Business card for new small company called "ZU"

I need a Business Card for new company out of Sacramento called "ZU". It is a mindful executive leadership training and mentoring company. The name "ZU" comes from the verb to "be". But the "ZU" is also a little play on phraseology, because historically I have had engineer sort of business cards that read "Marta Dunsby, P.E." for Professional Engineer. Now I want to be marta dunsby ZU - all sort of run together as shown in the file.

I didn't design a logo because I just want something simple in caps "ZU". I would like all the content included in the attached PowerPoint file. I would like the "ZU" lettering to be more rounded than that shown. I'd like it to be fun in some way. I'd also would like the "ZU" to be an object within the business card that I could use on letterhead, etc. And I'd love to have the card in fonts that I could get from Word or PowerPower point for example. I'm not attached to the particular fonts I've picked. Rather I just want kind of fun, but not unprofessional. I'd be pleased to have a second side with just a ZU on it. I have a blue color in mind for the ZU and am kind of thinking a blue background with white print. But if you have better ideas, please offer them.
Oh. Also, I'd like the text to be editable in something like adobe illustrator in case I need to change any of the details like my email address.

Target Market(s)

Executives who want to feel more alive and be more effective at their work

Industry/Entity Type

Leadership

Contact Information for Business Card

Simple card with "ZU" as the logo immediately following my name.

Colors
0493ce
3176b5

Requirements
Must have
• "ZU" in fun yet professional lettering. Other text as show in the uploaded file.
Nice to have
• back side with catchy color or placement.
Should not have
• more than one color in addition to white. - Want simple one-color design.

```html
<!DOCTYPE html>
<html lang="en">
<head>
<meta charset="utf-8">
<title>ZU — Business Card</title>
<link rel="stylesheet" href="https://fonts.googleapis.com/css2?family=Questrial&family=Quicksand:wght@400&family=Crimson+Text:ital@0;1&family=Shadows+Into+Light+Two&display=swap">
<style>
  :root {
    --zu-blue: #3176b5;
    --zu-blue-deep: #2f6ea8;
    --paper: #f2f1ed;
    --cream: #e4ded2;
    --backdrop: #eceeef;
  }
  * { margin: 0; padding: 0; box-sizing: border-box; }
  html, body { width: 1200px; height: 1000px; overflow: hidden; }
  body { background: var(--backdrop); position: relative; font-family: "Questrial", sans-serif; }

  .brand-word {
    position: absolute; left: 70px; top: 138px;
    font-family: "Questrial", sans-serif; font-size: 160px; line-height: 1;
    color: var(--zu-blue); letter-spacing: -2px; white-space: nowrap;
  }

  .banner-tagline {
    position: absolute; right: 54px; top: 74px;
    font-family: "Shadows Into Light Two", cursive; font-size: 18px;
    color: var(--zu-blue); white-space: nowrap;
  }
  .banner-square { position: absolute; right: 0; top: 56px; width: 40px; height: 59px; background: var(--zu-blue); }

  .side-note {
    position: absolute; left: 1160px; top: 952px; transform-origin: left top; transform: rotate(-90deg);
    font-family: "Quicksand", sans-serif; font-size: 15px; color: var(--zu-blue);
    white-space: nowrap; letter-spacing: 0.5px;
  }

  .card { position: absolute; width: 290px; height: 500px; box-shadow: 0 6px 18px rgba(0,0,0,0.12); }
  .card > * { position: absolute; left: 0; width: 100%; text-align: center; white-space: nowrap; }

  .card-front { left: 370px; top: 260px; background: var(--paper); color: var(--zu-blue-deep); }
  .card-front .logo-word { top: 58px; font-size: 76px; line-height: 1; }
  .card-front .name { top: 258px; font-family: "Quicksand", sans-serif; font-size: 26px; line-height: 1.2; }
  .card-front .role { top: 302px; font-family: "Crimson Text", serif; font-style: italic; font-size: 15px; }
  .card-front .contact { top: 344px; font-family: "Crimson Text", serif; font-size: 15px; line-height: 1.35; }
  .card-front .edge-square { top: auto; bottom: 0; left: 50%; width: 62px; height: 38px; margin-left: -31px; background: var(--zu-blue-deep); }

  .card-back { left: 720px; top: 200px; background: var(--zu-blue-deep); color: var(--cream); }
  .card-back .logo-word { top: 130px; font-size: 124px; line-height: 1; }
  .card-back .tagline { top: 350px; font-family: "Shadows Into Light Two", cursive; font-size: 16px; }
  .card-back .partnership { top: 402px; font-family: "Quicksand", sans-serif; font-size: 16px; }
</style>
</head>
<body>
  <div class="brand-word">ZU</div>

  <p class="banner-tagline">Be present, Lead well, Live it fully…</p>
  <div class="banner-square"></div>
  <p class="side-note">An Unlimited Partnership</p>

  <section class="card card-front">
    <div class="logo-word">ZU</div>
    <p class="name">Marta Dunsby ZU</p>
    <p class="role">Founder, Seeker</p>
    <p class="contact">(916) 555-0142<br>martadunsby@zuleadership.com</p>
    <div class="edge-square"></div>
  </section>

  <section class="card card-back">
    <div class="logo-word">ZU</div>
    <p class="tagline">Be present, Lead well, Live it fully…</p>
    <p class="partnership">An Unlimited Partnership</p>
  </section>
</body>
</html>
```